Expensive Jewelery and Gold Website

I require a one page template design for my site PrimeIngotHouse.example. We sell replica gold bars. Not real ones, they are novelty gifts.

I have several images of the bars (attached)
I would like a stylish and professional template layout that will be used on my site.

Designed to appear to businesses and professionals and not the members of the public.

There is no idenity or artwork for the business so you may use whichever scheme you wish to. But must somehow stylish use the images or 2-3 of the images attached.

Target Market(s)

Business and marketing professional.

Industry/Entity Type

Business

Requirements
Must have
• Incorporate some or all of images
Nice to have
• Colour/styled images to match design and look in-keeping

```html
<!DOCTYPE html>
<html lang="en">
<head>
<meta charset="utf-8">
<title>PrimeIngotHouse – Replica Gold Bars</title>
<link href="https://fonts.googleapis.com/css2?family=PT+Sans:ital,wght@0,400;0,700;1,400;1,700&family=Arimo:wght@400;700&display=swap" rel="stylesheet">
<style>
  :root {
    --ink-dark: #05090d;
    --glow-gold: #a88c3a;
    --gold: #f2b51f;
    --gold-deep: #d99a0c;
    --bar-top: #5a5a5a;
    --bar-bottom: #2e2e2e;
    --paper: #e4e4e4;
    --text: #444444;
    --text-soft: #555555;
    --white: #ffffff;
    --light: #d8d8d8;
    --panel: #2b2b2b;
    --rule: #c9c9c9;
  }
  * { box-sizing: border-box; margin: 0; padding: 0; }
  html, body { width: 1200px; height: 866px; overflow: hidden; }
  body {
    position: relative;
    background: var(--paper);
    font-family: "Arimo", Arial, sans-serif;
    color: var(--text);
  }
  .site-header {
    position: absolute; left: 0; top: 0; width: 1200px; height: 480px;
    background:
      radial-gradient(ellipse 560px 330px at 600px 40px, var(--glow-gold) 0%, #7a6528 35%, #2a2614 65%, rgba(5,9,13,0) 100%),
      linear-gradient(90deg, #0a1824 0%, var(--ink-dark) 20%, var(--ink-dark) 80%, #0a1824 100%);
  }
  .brand { position: absolute; left: 160px; top: 18px; }
  .brand-name {
    font-family: "PT Sans", sans-serif; font-weight: 700;
    font-size: 35px; color: #f1f1f1; letter-spacing: -0.5px; line-height: 40px;
  }
  .brand-tagline {
    font-family: "PT Sans", sans-serif; font-style: italic;
    font-size: 13px; color: #f3f3f3; margin-top: 0;
  }
  .account-links {
    position: absolute; right: 159px; top: 27px;
    font-size: 11.5px; color: #e8e8e8; word-spacing: 1px;
  }
  .account-links span { margin: 0 5px; }
  .main-nav {
    position: absolute; left: 150px; top: 99px; width: 900px; height: 49px;
    border-radius: 12px 12px 0 0;
    background: linear-gradient(#666 0%, var(--bar-top) 10%, var(--bar-bottom) 100%);
  }
  .main-nav a {
    position: absolute; top: 0; height: 49px; line-height: 51px;
    font-family: "PT Sans", sans-serif; font-style: italic; font-size: 15px;
    color: #f2f2f2; text-decoration: none; letter-spacing: -0.3px;
  }
  .main-nav a.is-active {
    background: linear-gradient(#f7c842, var(--gold) 60%, var(--gold-deep));
    color: #1c1c1c; padding: 0 8px;
  }
  .search {
    position: absolute; left: 715px; top: 15px; width: 168px; height: 22px;
    border-radius: 11px; background: #3d3d3d;
    box-shadow: inset 0 1px 3px rgba(0,0,0,.6);
    overflow: hidden;
  }
  .search-button {
    position: absolute; right: 0; top: 0; width: 41px; height: 22px;
    background: linear-gradient(#e6e6e6, #a9a9a9);
    border-radius: 0 11px 11px 0;
  }
  .search-button svg { position: absolute; left: 11px; top: 3px; }
  .products {
    position: absolute; left: 150px; top: 148px; width: 900px; height: 332px;
    display: flex;
  }
  .product { width: 225px; height: 332px; position: relative; border-right: 1px solid #555; }
  .product:last-child { border-right: none; }
  .product-image { height: 246px; }
  .img-gift { background: radial-gradient(circle at 45% 40%, #e4e4e6, #b9b8bc 60%, #8c8a8e); }
  .img-case-open { background: linear-gradient(150deg, #d9d3c9 0%, #7a3f1c 35%, #4a2410 70%, #8a4a22 100%); }
  .img-case-close { background: radial-gradient(circle at 50% 55%, #c9a040 0%, #201814 40%, #7a4018 80%, #b07a4a 100%); }
  .img-case-stack { background: linear-gradient(170deg, #d6cfc4 0%, #5a2c14 35%, #3a1c0c 70%, #6a3a20 100%); }
  .product-caption {
    height: 86px; padding: 11px 14px 0;
    background: linear-gradient(#555 0%, #3a3a3a 50%, #2a2a2a 100%);
    position: relative;
  }
  .product-title { font-family: "PT Sans", sans-serif; font-size: 17.5px; color: #e8e8e8; line-height: 22px; }
  .product-sub { font-size: 12px; color: #e6e6e6; margin-top: 1px; }
  .read-more {
    position: absolute; right: 15px; top: 53px; width: 82px; height: 23px;
    border-radius: 12px; background: linear-gradient(#ffffff, #d0d0d0 60%, #b8b8b8);
    box-shadow: 0 1px 2px rgba(0,0,0,.6);
    font-size: 13px; color: #333; text-align: center; line-height: 23px; letter-spacing: -0.4px;
  }
  .content-band {
    position: absolute; left: 0; top: 480px; width: 1200px; height: 110px;
    border-top: 2px solid #f4f4f4;
    background: radial-gradient(ellipse 500px 60px at 600px 20px, #dcd7c6, rgba(228,228,228,0));
  }
  .welcome-title {
    position: absolute; left: 150px; top: 508px;
    font-family: "PT Sans", sans-serif; font-style: italic; font-weight: 700;
    font-size: 35px; color: var(--text); letter-spacing: -1.6px;
  }
  .photo-stack { position: absolute; left: 152px; top: 553px; width: 242px; height: 200px; }
  .photo-back {
    position: absolute; left: 4px; top: 4px; width: 232px; height: 188px;
    background: var(--white); transform: rotate(2.2deg);
    box-shadow: 0 1px 4px rgba(0,0,0,.35);
  }
  .photo-front {
    position: absolute; left: 3px; top: 5px; width: 232px; height: 188px;
    background: var(--white); padding: 6px 5px 6px 6px;
    box-shadow: 0 1px 4px rgba(0,0,0,.4);
  }
  .photo-team {
    width: 221px; height: 176px;
    background: linear-gradient(90deg, #e8e4e0 0%, #2a2428 30%, #3c3c44 55%, #e6e6ea 75%, #3a3a44 100%);
  }
  .intro { position: absolute; left: 401px; top: 563px; width: 405px; font-size: 12.4px; line-height: 15.7px; color: var(--text-soft); }
  .intro p + p { margin-top: 15px; }
  .contact-box {
    position: absolute; left: 825px; top: 516px; width: 225px; height: 251px;
    background: linear-gradient(#3b3b3b, var(--panel) 40%, #1e1e1e);
  }
  .contact-title {
    height: 31px; padding: 4px 10px; border-bottom: 1px solid #555;
    font-family: "PT Sans", sans-serif; font-size: 17px; color: #f2f2f2;
  }
  .contact-intro { padding: 5px 8px 0; font-size: 10.8px; line-height: 16px; color: #eaeaea; }
  .field-label { position: absolute; left: 9px; font-size: 12px; color: #eee; }
  .field {
    position: absolute; left: 72px; width: 144px;
    background: linear-gradient(#ffffff, #e6e6e6);
    border: 1px solid #cfcfcf;
  }
  .submit {
    position: absolute; left: 140px; top: 213px; width: 76px; height: 28px;
    border-radius: 5px; background: linear-gradient(#f9cf4c, var(--gold) 55%, var(--gold-deep));
    font-family: "PT Sans", sans-serif; font-size: 15px; color: var(--white);
    text-align: center; line-height: 28px;
  }
  .site-footer {
    position: absolute; left: 150px; top: 778px; width: 900px;
    border-top: 1px solid var(--rule); padding-top: 15px;
    font-size: 12px; color: var(--text);
  }
  .footer-links span { margin: 0 7px; }
  .copyright { position: absolute; right: 0; top: 15px; }
</style>
</head>
<body>
  <header class="site-header">
    <div class="brand">
      <div class="brand-name">PrimeIngotHouse</div>
      <div class="brand-tagline">The Best Choice on The Web</div>
    </div>
    <div class="account-links">My Account<span>|</span>My Wishlist<span>|</span>My Cart<span>|</span>Checkout<span>|</span>Log In</div>

    <nav class="main-nav">
      <a style="left:25px">Home</a>
      <a style="left:80px">About Us</a>
      <a class="is-active" style="left:146px">Our Products</a>
      <a style="left:251px">Support</a>
      <a style="left:318px">Testimonials</a>
      <a style="left:410px">Contact Us</a>
      <div class="search">
        <div class="search-button">
          <svg width="20" height="16" viewBox="0 0 20 16"><circle cx="7" cy="7" r="5" fill="none" stroke="#333" stroke-width="2.2"/><line x1="11" y1="10" x2="17" y2="14" stroke="#333" stroke-width="2.6" stroke-linecap="round"/></svg>
        </div>
      </div>
    </nav>

    <section class="products">
      <article class="product">
        <div class="product-image img-gift" role="img" aria-label="Gift box wrapped in silver paper with an organza ribbon"></div>
        <div class="product-caption"><div class="product-title">Replica gold bar product</div><div class="product-sub">All products</div><div class="read-more">read more</div></div>
      </article>
      <article class="product">
        <div class="product-image img-case-open" role="img" aria-label="Open wooden presentation case holding a replica gold bar"></div>
        <div class="product-caption"><div class="product-title">Replica gold bar product</div><div class="product-sub">All products</div><div class="read-more">read more</div></div>
      </article>
      <article class="product">
        <div class="product-image img-case-close" role="img" aria-label="Close view of a replica gold bar in a clear case on black velvet"></div>
        <div class="product-caption"><div class="product-title">Replica gold bar product</div><div class="product-sub">All products</div><div class="read-more">read more</div></div>
      </article>
      <article class="product">
        <div class="product-image img-case-stack" role="img" aria-label="Stacked wooden gift cases with one open showing a gold bar"></div>
        <div class="product-caption"><div class="product-title">Replica gold bar product</div><div class="product-sub">All products</div><div class="read-more">read more</div></div>
      </article>
    </section>
  </header>

  <div class="content-band"></div>

  <h1 class="welcome-title">Welcome to PrimeIngotHouse</h1>

  <div class="photo-stack">
    <div class="photo-back"></div>
    <div class="photo-front"><div class="photo-team" role="img" aria-label="Team of business professionals standing together"></div></div>
  </div>

  <div class="intro">
    <p>Lorem ipsum dolor sit amet, consectetur adipisicing elit, sed do eius-mod tempor incididunt ut labore et dolore magna aliqua. Ut enim ad minim veniam, quis nostrud exercitation ullamco laboris nisi ut aliquip ex ea commodo consequat. Duis aute irure dolor in reprehenderit in voluptate velit esse cillum dolore eu fugiat nulla pariatur.</p>
    <p>Lorem ipsum dolor sit amet, consectetur adipisicing elit, sed do eius-mod tempor incididunt ut labore et dolore magna aliqua. Ut enim ad minim veniam, quis nostrud exercitation ullamco laboris nisi ut aliquip ex ea commodo consequat. Duis aute irure dolor in reprehenderit in voluptate velit esse cillum dolore eu fugiat nulla pariatur.Lorem ipsum dolor sit amet, consectetur adipisicing elit.</p>
  </div>

  <aside class="contact-box">
    <div class="contact-title">Contact us</div>
    <div class="contact-intro">It is a long established fact that a reader will be distracted by the.</div>
    <span class="field-label" style="top:87px">Name:</span>
    <div class="field" style="top:83px;height:24px"></div>
    <span class="field-label" style="top:115px">Email:</span>
    <div class="field" style="top:111px;height:24px"></div>
    <span class="field-label" style="top:143px">Comment:</span>
    <div class="field" style="top:139px;height:68px"></div>
    <div class="submit">SUBMIT</div>
  </aside>

  <footer class="site-footer">
    <div class="footer-links">Home<span>|</span>About Us<span>|</span>Our Products <span>|</span>Support<span>|</span>Testimonials<span>|</span>Contact Us</div>
    <div class="copyright">Copyright © 2010 PrimeIngotHouse.example . All Rights Reserved.</div>
  </footer>
</body>
</html>
```